Website design for Harbourline Bag printing specialist

We need an overhaul of our website front end design. We need a new look and a modern take on the products we sell and service we offer. We sell plain stock in a variety of bag types and offer a printing service of customers branding and logos. Customers request online quotes and this facility must be an easy one step process for users. Our logo is currently green and orange and we are not really looking for re branding at this stage. The final design must communicate that we are the leading printing specialist throughout the country, have been in operation for 15 years and have a vast amount of experience and expertise. The design must instantly show the products available and the ability to request a quote for the desired product.

Target Market(s)

Trade shows, retailers, dentists, food suppliers. wine makers etc etc and anyone that uses carry bags

Industry/Entity Type

Screen Printing

Number of Pages Required

5+ page

Font styles to use
Serif
Sans Serif

Colors

Designer to choose colors to be used in the design.

Requirements
Must have
• Our home page featuring all the products as selectable entities and a short description of what each bag type is when the user hovers over the image.
• Then the product landing pages must show different sizes of that product type. On each page there must be a quick quote button that goes to the quote screen with the features and information to select or include for a quote to be processed. The logo is green and orange and still should have this present but happy to move away from this on the website pages in general.I have so many product pictures and unable to upload them all here. The categories for products are as follows:
• Kraft Paper Bags
• Laminated bags
• Non-woven bags
• Calico bags
• Wine bags
• Florist bags
• Plastic Bags
• Printed Bags
• Gift Boxes
• Tissue paper
• Wrapping Paper
• Custom Bags and Boxes
• There also needs to be a gallery page that showcases work we have done. The ability to have a description for each photo in the gallery would be great.
• A general bag size page would be great and one content page that is about us and another for contact us.
• A free sample button so a user can request a sample. Phone number must be included on this page and unable to submit with a valid phone number.
• Our phone number should be prominent.
• A search feature please.
Nice to have
• Fonts should be in keeping with the design of the website
Should not have
• I dont want users having to scroll too far down to find information. The icons of the bags on the home screen should almost appear on one screen.
• I can upload all my content and pictures so no need to get them from me. I really want your look and feel and design layout that i can then work from.

```html
<!DOCTYPE html>
<html lang="en">
<head>
<meta charset="utf-8">
<title>Harbourline Bag – Bag Printing Specialist</title>
<link rel="stylesheet" href="https://fonts.googleapis.com/css2?family=Roboto:wght@400;500;700;900&display=swap">
<style>
:root{
  --orange:#f0791c;
  --green-dark:#1d5a2a;
  --green-mid:#2c7339;
  --green-btn:#6cb42e;
  --ink:#2d2d2d;
  --muted:#7a7a7a;
  --line:#dedede;
  --soft:#f3f3f3;
  --footer:#2a2a2a;
  --white:#ffffff;
}
*{box-sizing:border-box;margin:0;padding:0}
html,body{width:1200px;height:4945px;overflow:hidden}
body{font-family:"Roboto",Arial,sans-serif;color:var(--ink);background:var(--white)}

/* top bar */
.topbar{height:40px;background:var(--orange);display:flex;justify-content:flex-end;align-items:stretch;padding-right:110px;font-size:13px;font-weight:700;color:var(--white);text-transform:uppercase}
.topbar .call{display:flex;align-items:center;gap:8px;padding-right:28px}
.topbar .call strong{font-size:20px}
.topbar .sample{background:#b9561a;display:flex;align-items:center;padding:0 22px}
.topbar .quote{background:var(--green-btn);display:flex;align-items:center;padding:0 22px}

/* header */
.header{height:108px;display:flex;align-items:center;justify-content:space-between;padding:0 112px}
.brand{display:flex;align-items:center;gap:10px;font-size:26px;font-weight:700;color:var(--green-dark)}
.brand .dot{width:22px;height:22px;border-radius:50%;background:var(--orange)}
.nav{display:flex;align-items:center;gap:34px;font-size:14px;font-weight:700;text-transform:uppercase}
.nav a{color:var(--ink);text-decoration:none}
.nav a.active{color:var(--green-btn)}

/* hero */
.hero{position:relative;height:604px;background:linear-gradient(135deg,#6d7f96 0%,#a6b4c3 35%,#d9b7c6 60%,#b88f6a 100%);text-align:center;color:var(--white)}
.hero h1{padding-top:58px;font-size:58px;font-weight:700;letter-spacing:1px}
.hero p{margin-top:12px;font-size:22px}
.hero .btn{display:inline-block;margin-top:28px;padding:13px 28px;border:2px solid var(--white);border-radius:30px;background:rgba(255,255,255,.2);font-size:14px;font-weight:700;text-transform:uppercase}
.hero .arrow{position:absolute;top:430px}
.hero .arrow.left{left:48px}
.hero .arrow.right{right:48px}

/* categories */
.categories{height:1879px;padding-top:100px}
.section-title{text-align:center;font-size:41px;font-weight:700;color:var(--green-dark);line-height:50px;text-transform:uppercase}
.grid{margin:54px auto 0;width:976px;display:grid;grid-template-columns:repeat(3,313px);column-gap:18px;row-gap:30px}
.card{height:370px;border:1px solid var(--line);border-radius:4px;padding:10px;text-align:center;box-shadow:0 2px 4px rgba(0,0,0,.06)}
.card .photo{height:195px;background:#ececec}
.card h3{margin-top:28px;font-size:19px;font-weight:700}
.card p{margin:10px auto 0;width:260px;font-size:13px;line-height:20px;color:var(--muted)}
.card .more{display:block;margin:12px auto 0;width:18px;height:18px}

/* welcome */
.welcome{height:551px;background:var(--soft);padding-top:86px;text-align:center}
.welcome .lead{margin:28px auto 0;width:780px;font-size:15px;line-height:28px;color:var(--muted)}
.features{margin:38px auto 0;width:976px;display:flex;justify-content:space-between}
.feature{width:470px;height:142px;background:var(--white);border:1px solid var(--line);display:flex;gap:22px;padding:28px 24px;text-align:left}
.feature h4{font-size:21px;font-weight:500}
.feature p{margin-top:10px;font-size:13px;line-height:20px;color:var(--muted)}

/* testimonials */
.testimonials{height:544px;background:linear-gradient(120deg,#1b5027 0%,#26693a 60%,#2f7a45 100%);text-align:center;color:var(--white);padding-top:80px}
.testimonials .section-title{color:var(--white)}
.stars{margin-top:16px}
.testimonials blockquote{margin:26px auto 0;width:760px;font-size:15px;font-style:italic;line-height:28px;color:#dfe9df}
.avatars{margin-top:40px;display:flex;justify-content:center;align-items:center;gap:14px}
.avatar{border-radius:50%;background:linear-gradient(#c7b49c,#8a7563);border:4px solid rgba(255,255,255,.5)}
.avatar.small{width:84px;height:84px;opacity:.7}
.avatar.big{width:100px;height:100px;border-color:var(--white)}
.testimonials .name{margin-top:14px;font-size:17px;font-weight:500;text-transform:uppercase}
.testimonials .role{margin-top:6px;font-size:13px;color:#cfe0cf}

/* gallery */
.gallery{height:890px;padding-top:93px;text-align:center}
.gallery-rows{margin:44px auto 0;width:976px}
.gallery-row{display:flex;gap:13px;margin-bottom:13px}
.gallery-row div{height:234px}
.view-more{display:inline-block;margin-top:52px;width:175px;line-height:58px;border-radius:30px;background:var(--green-btn);color:var(--white);font-size:15px;font-weight:700;text-transform:uppercase}

/* footer */
.footer{height:329px;background:var(--footer);color:#d0d0d0;text-align:center;padding-top:82px;font-size:13px}
.social{display:flex;justify-content:center;gap:14px}
.social span{width:46px;height:46px;border:2px solid #d0d0d0;border-radius:50%}
.contact-line{margin-top:24px;display:flex;justify-content:center;gap:14px;align-items:center}
.links{margin-top:30px;display:flex;justify-content:center;gap:18px}
.copy{margin-top:30px}
</style>
</head>
<body>

<div class="topbar">
  <div class="call">Call for a free quote <strong>1300 555 014</strong></div>
  <div class="sample">Free Sample</div>
  <div class="quote">Online Quote</div>
</div>

<header class="header">
  <div class="brand"><span class="dot"></span>Harbourline Bag</div>
  <nav class="nav">
    <a class="active">Home</a><a>About Us</a><a>Gallery</a><a>Bag Size</a><a>Contact Us</a>
    <svg width="16" height="16" viewBox="0 0 16 16"><circle cx="6.5" cy="6.5" r="5" fill="none" stroke="#2d2d2d" stroke-width="2"/><line x1="10" y1="10" x2="15" y2="15" stroke="#2d2d2d" stroke-width="2"/></svg>
  </nav>
</header>

<section class="hero" role="img" aria-label="Colourful shopping bags in a bright retail setting">
  <h1>HARBOURLINE BAG</h1>
  <p>At vero eos et accusamus et iusto odio dignissimos ducim</p>
  <span class="btn">Get a Quote</span>
  <svg class="arrow left" width="20" height="34" viewBox="0 0 20 34"><polyline points="17,3 3,17 17,31" fill="none" stroke="#fff" stroke-width="3"/></svg>
  <svg class="arrow right" width="20" height="34" viewBox="0 0 20 34"><polyline points="3,3 17,17 3,31" fill="none" stroke="#fff" stroke-width="3"/></svg>
</section>

<section class="categories">
  <h2 class="section-title">Categories</h2>
  <div class="grid">
    <div class="card"><div class="photo" role="img" aria-label="Brown kraft paper bag" style="background:#eceae6"></div><h3>Kraft Paper Bags</h3><p>Strong, environmentally friendly brown, white and coloured reusable kraft bags</p><svg class="more" viewBox="0 0 18 18"><circle cx="9" cy="9" r="9" fill="#f0791c"/><path d="M9 5v8M5 9h8" stroke="#fff" stroke-width="2"/></svg></div>
    <div class="card"><div class="photo" role="img" aria-label="Black laminated bag" style="background:#e9e9ea"></div><h3>Laminated bags</h3><p>High quality matte or gloss laminated bags for corporate, boutique and events</p><svg class="more" viewBox="0 0 18 18"><circle cx="9" cy="9" r="9" fill="#f0791c"/><path d="M9 5v8M5 9h8" stroke="#fff" stroke-width="2"/></svg></div>
    <div class="card"><div class="photo" role="img" aria-label="Blue non-woven tote bag" style="background:#e6ebee"></div><h3>Non-woven bags</h3><p>Eco-friendly, recyclable, reusable display of your brand</p><svg class="more" viewBox="0 0 18 18"><circle cx="9" cy="9" r="9" fill="#f0791c"/><path d="M9 5v8M5 9h8" stroke="#fff" stroke-width="2"/></svg></div>
    <div class="card"><div class="photo" role="img" aria-label="Natural calico tote bag" style="background:#efece7"></div><h3>Calico bags</h3><p>Natural or black 100% cotton calico bags plain or printed wholesale supplied</p><svg class="more" viewBox="0 0 18 18"><circle cx="9" cy="9" r="9" fill="#f0791c"/><path d="M9 5v8M5 9h8" stroke="#fff" stroke-width="2"/></svg></div>
    <div class="card"><div class="photo" role="img" aria-label="Wine bottle gift bag" style="background:#ebe8e4"></div><h3>Wine bags</h3><p>Wine gift bags add style to wine bottles and make a great gift wrapping option</p><svg class="more" viewBox="0 0 18 18"><circle cx="9" cy="9" r="9" fill="#f0791c"/><path d="M9 5v8M5 9h8" stroke="#fff" stroke-width="2"/></svg></div>
    <div class="card"><div class="photo" role="img" aria-label="Patterned florist bag with flowers" style="background:#efe9e8"></div><h3>Florist bags</h3><p>Nam libero tempore, cum soluta nobis est eligendi optio cumque nihil</p><svg class="more" viewBox="0 0 18 18"><circle cx="9" cy="9" r="9" fill="#f0791c"/><path d="M9 5v8M5 9h8" stroke="#fff" stroke-width="2"/></svg></div>
    <div class="card"><div class="photo" role="img" aria-label="Clear plastic carry bag" style="background:#eeeeee"></div><h3>Plastic Bags</h3><p>Our plastic bags are practical, affordable and stylish with a variety of sizes.</p><svg class="more" viewBox="0 0 18 18"><circle cx="9" cy="9" r="9" fill="#f0791c"/><path d="M9 5v8M5 9h8" stroke="#fff" stroke-width="2"/></svg></div>
    <div class="card"><div class="photo" role="img" aria-label="Group of colourful printed bags" style="background:#e8ece6"></div><h3>Printed Bags</h3><p>Increase your brand visibility with custom-tool printed bags using your artwork</p><svg class="more" viewBox="0 0 18 18"><circle cx="9" cy="9" r="9" fill="#f0791c"/><path d="M9 5v8M5 9h8" stroke="#fff" stroke-width="2"/></svg></div>
    <div class="card"><div class="photo" role="img" aria-label="Brown cardboard gift box" style="background:#ece8e4"></div><h3>Gift Boxes</h3><p>Our boxes come in classic brown, crisp white as well as a range of vibrant colours</p><svg class="more" viewBox="0 0 18 18"><circle cx="9" cy="9" r="9" fill="#f0791c"/><path d="M9 5v8M5 9h8" stroke="#fff" stroke-width="2"/></svg></div>
    <div class="card"><div class="photo" role="img" aria-label="Rolls of coloured tissue paper" style="background:#efe9e6"></div><h3>Tissue paper</h3><p>Tissue paper adds luxury feel to beautifully wrapped gifts in carry bags</p><svg class="more" viewBox="0 0 18 18"><circle cx="9" cy="9" r="9" fill="#f0791c"/><path d="M9 5v8M5 9h8" stroke="#fff" stroke-width="2"/></svg></div>
    <div class="card"><div class="photo" role="img" aria-label="Rolls of coloured wrapping paper" style="background:#e8ebec"></div><h3>Wrapping Paper</h3><p>Wrapping paper to complement your other products</p><svg class="more" viewBox="0 0 18 18"><circle cx="9" cy="9" r="9" fill="#f0791c"/><path d="M9 5v8M5 9h8" stroke="#fff" stroke-width="2"/></svg></div>
    <div class="card"><div class="photo" role="img" aria-label="Jute custom bag with green trim" style="background:#ebe9e3"></div><h3>Custom Bags and Boxes</h3><p>Custom made bags and boxes, personalised custom gift boxes, bags</p><svg class="more" viewBox="0 0 18 18"><circle cx="9" cy="9" r="9" fill="#f0791c"/><path d="M9 5v8M5 9h8" stroke="#fff" stroke-width="2"/></svg></div>
  </div>
</section>

<section class="welcome">
  <h2 class="section-title">Welcome to Harbourline Bag</h2>
  <p class="lead">The packaging of your products is in the bag with Harbourline Bag. Harbourline Bag is a growing leader in retail packaging for Australia. Also supplying plain stock, our range of bags and custom made boxes are perfect for companies looking for wholesale solutions to their packaging needs.</p>
  <div class="features">
    <div class="feature">
      <svg width="46" height="40" viewBox="0 0 46 40"><path d="M2 4h18l22 22-14 14L6 18z" fill="#f0791c"/><circle cx="11" cy="12" r="3" fill="#fff"/></svg>
      <div><h4>Selling variety of bags</h4><p>Nam libero tempore, cum soluta nobis est eligendi optio cumque nihil impedit quo</p></div>
    </div>
    <div class="feature">
      <svg width="46" height="40" viewBox="0 0 46 40"><rect x="12" y="2" width="22" height="10" fill="#f0791c"/><rect x="3" y="13" width="40" height="16" rx="3" fill="#f0791c"/><rect x="12" y="24" width="22" height="14" fill="#fff" stroke="#f0791c" stroke-width="3"/></svg>
      <div><h4>Printing branding and logos</h4><p>Nam libero tempore, cum soluta nobis est eligendi optio cumque nihil impedit quo</p></div>
    </div>
  </div>
</section>

<section class="testimonials" role="region" aria-label="Testimonials over a soft green shopping bag backdrop">
  <h2 class="section-title">Testimonials</h2>
  <svg class="stars" width="110" height="20" viewBox="0 0 110 20">
    <g fill="#fff"><polygon points="10,1 12.6,7 19,7.5 14,11.8 15.6,18 10,14.6 4.4,18 6,11.8 1,7.5 7.4,7"/><polygon transform="translate(22 0)" points="10,1 12.6,7 19,7.5 14,11.8 15.6,18 10,14.6 4.4,18 6,11.8 1,7.5 7.4,7"/><polygon transform="translate(44 0)" points="10,1 12.6,7 19,7.5 14,11.8 15.6,18 10,14.6 4.4,18 6,11.8 1,7.5 7.4,7"/><polygon transform="translate(66 0)" points="10,1 12.6,7 19,7.5 14,11.8 15.6,18 10,14.6 4.4,18 6,11.8 1,7.5 7.4,7"/></g>
    <polygon transform="translate(88 0)" points="10,1 12.6,7 19,7.5 14,11.8 15.6,18 10,14.6 4.4,18 6,11.8 1,7.5 7.4,7" fill="none" stroke="#fff" stroke-width="1.5"/>
  </svg>
  <blockquote>Nemo enim ipsam voluptatem quia voluptas sit aspernatur aut odit aut fugit, sed quia consequuntur magni dolores eos qui ratione voluptatem sequi porro quisquam est, qui dolorem ipsum quia di</blockquote>
  <div class="avatars">
    <div class="avatar small" role="img" aria-label="Customer portrait"></div>
    <div class="avatar big" role="img" aria-label="Portrait of Maya"></div>
    <div class="avatar small" role="img" aria-label="Customer portrait"></div>
  </div>
  <div class="name">Maya</div>
  <div class="role">Upsam voluptate</div>
</section>

<section class="gallery">
  <h2 class="section-title">Gallery</h2>
  <div class="gallery-rows">
    <div class="gallery-row">
      <div style="width:442px;background:linear-gradient(135deg,#8a6a4f,#c9a37f,#7d8c5a)" role="img" aria-label="Hands holding colourful shopping bags"></div>
      <div style="width:254px;background:linear-gradient(135deg,#e9b99a,#c98a62)" role="img" aria-label="Kraft paper bag on peach background"></div>
      <div style="width:254px;background:linear-gradient(135deg,#6a4a3c,#b7906c,#4f3a30)" role="img" aria-label="Rolls of patterned wrapping paper"></div>
    </div>
    <div class="gallery-row">
      <div style="width:317px;background:linear-gradient(135deg,#e8e2dc,#c84a4a,#efe9e2)" role="img" aria-label="Gift box with red ribbon held in hands"></div>
      <div style="width:317px;background:linear-gradient(135deg,#d8c7a6,#eadcc0)" role="img" aria-label="Close-up of a calico bag handle"></div>
      <div style="width:316px;background:linear-gradient(135deg,#3c8ec4,#7cc3a0,#f0d84a,#8a4ea8)" role="img" aria-label="Colourful tissue paper sheets"></div>
    </div>
  </div>
  <span class="view-more">View More</span>
</section>

<footer class="footer">
  <div class="social" aria-label="Social links"><span></span><span></span><span></span><span></span></div>
  <div class="contact-line">
    <svg width="10" height="14" viewBox="0 0 10 14"><path d="M5 0a5 5 0 0 1 5 5c0 4-5 9-5 9S0 9 0 5a5 5 0 0 1 5-5z" fill="#d0d0d0"/><circle cx="5" cy="5" r="2" fill="#2a2a2a"/></svg>
    <span>PO Box 118, Eastvale Vic, 3999</span><span>|</span>
    <svg width="13" height="13" viewBox="0 0 13 13"><path d="M3 0l2 3-1.5 1.5a8 8 0 0 0 5 5L10 8l3 2-1 3C5 13 0 8 0 1z" fill="#d0d0d0"/></svg>
    <span>1300 555 014</span><span>|</span>
    <svg width="15" height="11" viewBox="0 0 15 11"><rect width="15" height="11" fill="#d0d0d0"/><polyline points="0,0 7.5,6 15,0" fill="none" stroke="#2a2a2a" stroke-width="1.5"/></svg>
    <span>hello@harbourlinebag.com.au</span>
  </div>
  <div class="links"><span>Help</span><span>|</span><span>FAQ</span><span>|</span><span>Shipping</span><span>|</span><span>Returns &amp; Replacement Policy</span><span>|</span><span>Terms Of Use</span><span>|</span><span>Privacy Statement</span></div>
  <div class="copy">Harbourline Bag © 2019 All rights reserved.</div>
</footer>

</body>
</html>
```